Presentation & Communication (Guide, Ebook, carroussel vistelle, corvanet et plumora)

Suite à la conception du logo, je souhaite désormais développer une identité visuelle complète ainsi que des supports marketing pour ma page Plumora, ma communication client interne notamment :
- Couverture Plumora + Photo de profil Plumora
- Guides
- E-books
- Et enfin, une charte graphique destinée aux formulaires sous format Microsoft Forms (pour la collecte de sondages et la prospection).
Vous trouverez ci-joint le logo que vous avez créé, ainsi qu’une couverture que j’ai réalisée via Canva. Cependant, lors de l’importation sur Plumora, le logo et les illustrations apparaissent flous.
Rappel important :
La direction artistique et l’identité visuelle doivent être en parfaite cohérence avec le logo et l’activité, à savoir :
un cabinet d’expertise comptable spécialisé pour les chirurgiens-dentistes et les centres dentaires. Je souhaite quelque chose de minimaliste, haut de gamme et moderne (je veux pas des logos de dents et d'instrument grossier et dans tous les sens).
Les couleurs qui ont été utilisées pour le site sont principalement : #0F1121 ; #FFFFFF ; #4A90A4 ; #5FAFB3.
Les supports doivent être téléchargeable sous format pack office de façon à pouvoir les utiliser et rédiger dessus du texte (guides, e-books, image pour post réseaux sociaux). Il faut donc déterminer une police efficace qui correspond à l'image de mon cabinet comptable (Poppins peut être ?)
Ce que j'aimerais :
1) Une visuel de page de couverture Plu mora
2) Un visuel d'image de profil (Icône) de page Plumora / Vistelle de mon logo
3) Un visuel moderne, haut de gamme et élégant au bon format en utilsant en partie les couleurs évoqué dans le brief. Ce visuel doit être adaptée au format Post publication Vistelle et Plumora avec un visuel autour mais avec la possibilité d'écrire du texte sur le support que vous créér (exemple pièce jointe d'un confrère à moi)
4) Un support Guide de façon également à rédiger dessus simplement avec une bonne typographie moderne et professionnelle, sur plusieurs pages à minima sur 10 pages. Je demande un peu la création d'un thème sous format pack office pour simplifier l'utilisation du fichier et le process pour uniquement éditer et importer sur CorvaNet, Plumora et Vistelle sans transformer ou redymensionner ou rogner la qualité du support. (Deux Exemples ci-joint).
5) Créer un Ebook de la même manière avec un fond (un thème) qui représente bien mon cabinet haut de gamme, classe et moderne. (Exemple Ebook ci-joint)
English :
Following the logo design, I now wish to develop a complete visual identity and marketing materials for my Plumora page and internal client communications, including:
- Plumora cover photo + Plumora profile picture
- Guides
- E-books
- And finally, a style guide for Microsoft Forms forms (for survey collection and lead generation).
Attached you will find the logo you created, as well as a cover photo I designed using Canva. However, when uploaded to Plumora, the logo and illustrations appear blurry.
Important reminder:
The art direction and visual identity must be perfectly consistent with the logo and the business activity, namely:
an accounting firm specializing in services for dentists and dental clinics. I want something minimalist, high-end, and modern (I don't want logos of teeth and crude instruments in all directions).
The colors used for the website are primarily: #0F1121; #FFFFFF; #4A90A4; #5FAFB3.
The materials must be downloadable in Microsoft Office format so they can be used and text added to (guides, e-books, images for social media posts). Therefore, an effective font that matches my accounting firm's image needs to be chosen (Poppins, perhaps?).
What I would like:
1) A Plumora cover image
2) A Plumora/Vistelle profile picture (icon) of my logo
3) A modern, high-end, and elegant image in the correct format, partially using the colors mentioned in the brief. This image must be suitable for Vistelle and Plumora posts, with a surrounding image, but with the option to write text on the document you create (example attached from a colleague).
4) A guide template, also easy to write on, with good, modern, and professional typography, spanning at least 10 pages. I would like a template created in Microsoft Office format to simplify file use and the process of simply editing and importing it to CorvaNet, Plumora, and Vistelle without transforming, resizing, or cropping the document. (Two examples attached).
5) Create an ebook in the same style with a background (theme) that accurately represents my high-end, classy, and modern firm. (Example ebook attached)
Chirurgiens dentistes, orthodontistes
Expertise comptable et conseil fiscal

```html
<!DOCTYPE html>
<html lang="fr">
<head>
<meta charset="utf-8">
<title>Couverture de page – Cabinet expertise comptable dentaire</title>
<link href="https://fonts.googleapis.com/css2?family=Poppins:wght@500;700&display=swap" rel="stylesheet">
<style>
  :root {
    --navy: #161a2e;
    --navy-deep: #0f1121;
    --sand: #e8e0d0;
    --white: #ffffff;
    --skin: #d9b9a3;
    --clinic-blue: #8fb7cf;
  }
  html, body {
    margin: 0;
    padding: 0;
    width: 1200px;
    height: 600px;
    overflow: hidden;
    background: var(--navy-deep);
  }
  .cover {
    position: relative;
    width: 1200px;
    height: 600px;
    overflow: hidden;
    background: var(--navy);
    font-family: "Poppins", sans-serif;
  }
  .cover__backdrop {
    position: absolute;
    inset: 0;
    background:
      radial-gradient(ellipse 520px 380px at 300px 260px, rgba(120,125,150,0.22), transparent 70%),
      linear-gradient(90deg, #22263a 0%, var(--navy) 55%, var(--navy-deep) 100%);
  }
  .cover__headline {
    position: absolute;
    left: 88px;
    top: 150px;
    margin: 0;
    font-size: 47px;
    line-height: 66px;
    font-weight: 500;
    color: var(--white);
    letter-spacing: 0.2px;
  }
  .cover__headline .accent {
    color: var(--sand);
    font-weight: 700;
  }
  .cover__headline span.line { display: block; }
  .cover__portraits {
    position: absolute;
    inset: 0;
  }
</style>
</head>
<body>
  <main class="cover">
    <div class="cover__backdrop" role="img" aria-label="Photo en fondu d'un soin dentaire, teintes bleu nuit"></div>

    <h1 class="cover__headline">
      <span class="line accent">Spécialistes</span>
      <span class="line"><span class="accent">Du Développement</span> Et</span>
      <span class="line">De La Fiscalité Des</span>
      <span class="line">Chirurgiens-dentistes</span>
    </h1>

    <svg class="cover__portraits" width="1200" height="600" viewBox="0 0 1200 600">
      <defs>
        <linearGradient id="patientTones" x1="0" y1="0" x2="1" y2="1">
          <stop offset="0" stop-color="#e6cbb6"/>
          <stop offset="0.55" stop-color="#c99d85"/>
          <stop offset="1" stop-color="#8fb7cf"/>
        </linearGradient>
        <linearGradient id="clinicTones" x1="0" y1="0" x2="1" y2="1">
          <stop offset="0" stop-color="#8fb7cf"/>
          <stop offset="0.5" stop-color="#e0c4b0"/>
          <stop offset="1" stop-color="#dfe6ee"/>
        </linearGradient>
      </defs>

      <!-- large portrait -->
      <circle cx="940" cy="500" r="300" fill="var(--sand)"/>
      <circle cx="940" cy="500" r="286" fill="var(--navy-deep)"/>
      <circle cx="940" cy="500" r="272" fill="url(#patientTones)" role="img" aria-label="Photo d'une patiente souriante pendant un examen dentaire"/>

      <!-- small portrait -->
      <circle cx="1090" cy="150" r="160" fill="var(--navy-deep)"/>
      <circle cx="1090" cy="150" r="148" fill="var(--sand)"/>
      <circle cx="1090" cy="150" r="136" fill="url(#clinicTones)" role="img" aria-label="Photo d'une patiente chez le chirurgien-dentiste"/>
    </svg>
  </main>
</body>
</html>
```